Corvelle vineyards

Wine label/logo that is old world witH a modern Maybe Latin/Hispanic twist. Nothing cartoonish or colorful.

This is a wine vineyard growing tempranillo, Malbec, cabarnet. I am looking for a wine label that incorporates the logo for Corvelle Vineyards. Location Temecula california

```html
<!DOCTYPE html>
<html lang="en">
<head>
<meta charset="utf-8">
<title>Corvelle Vineyards — Wine Labels</title>
<link href="https://fonts.googleapis.com/css2?family=Cinzel:wght@400&family=Montserrat:wght@300;500&display=swap" rel="stylesheet">
<style>
  :root {
    --canvas: #000000;
    --label-white: #ffffff;
    --label-silver: #e6e6e8;
    --label-slate: #6d6e71;
    --ink: #231f20;
    --ink-light: #ffffff;
    --gold: #dccb8a;
    --rule-dark: #4a4748;
    --rule-light: #8a8b8e;
  }
  html, body {
    margin: 0;
    padding: 0;
    width: 1200px;
    height: 1200px;
    overflow: hidden;
    background: var(--canvas);
  }
  .label-row {
    position: relative;
    width: 1200px;
    height: 1200px;
  }
  .label {
    position: absolute;
    top: 334px;
    width: 343px;
    height: 530px;
    color: var(--ink);
    --rule: var(--rule-dark);
  }
  .label--tempranillo { left: 38px; background: var(--label-white); }
  .label--malbec { left: 435px; background: var(--label-silver); }
  .label--cabernet { left: 818px; background: var(--label-slate); color: var(--ink-light); --rule: var(--rule-light); }

  .brand-square {
    position: absolute;
    top: 127px;
    left: 151px;
    width: 40px;
    height: 52px;
    background: var(--gold);
  }
  .brand-name {
    position: absolute;
    left: 0;
    width: 100%;
    text-align: center;
    font-family: "Cinzel", serif;
    font-weight: 400;
    color: inherit;
    margin: 0;
  }
  .brand-name__main {
    top: 196px;
    font-size: 29px;
    letter-spacing: 15px;
    padding-left: 15px;
    box-sizing: border-box;
    line-height: 1;
  }
  .brand-name__sub {
    top: 235px;
    font-size: 9px;
    letter-spacing: 3.2px;
    padding-left: 3px;
    box-sizing: border-box;
    line-height: 1;
  }

  .varietal {
    position: absolute;
    top: 382px;
    left: 95px;
    width: 153px;
    font-family: "Montserrat", sans-serif;
  }
  .varietal--centered { left: 95px; text-align: center; }
  .varietal__name {
    font-weight: 300;
    font-size: 14.5px;
    line-height: 21px;
    height: 22px;
    border-bottom: 1px solid var(--rule);
    white-space: nowrap;
    display: flex;
    align-items: center;
  }
  .varietal--centered .varietal__name { justify-content: center; }
  .label--cabernet .varietal {
    left: 70px;
    width: 203px;
  }
  .label--cabernet .varietal__name { border-bottom-color: rgba(255,255,255,0.15); }
  .varietal__divider {
    display: inline-block;
    width: 1px;
    height: 20px;
    background: var(--rule);
    margin: 0 8px 0 8px;
  }
  .varietal__origin {
    margin-top: 5px;
    font-weight: 500;
    font-size: 7.5px;
    letter-spacing: 0;
    white-space: nowrap;
  }
</style>
</head>
<body>
<main class="label-row">

  <section class="label label--tempranillo">
    <div class="brand-square"></div>
    <p class="brand-name brand-name__main">CORVELLE</p>
    <p class="brand-name brand-name__sub">VINEYARDS</p>
    <div class="varietal">
      <div class="varietal__name">TEMPRANILLO<span class="varietal__divider"></span>2018</div>
      <div class="varietal__origin">TEMECULA , CALIFORNIA</div>
    </div>
  </section>

  <section class="label label--malbec">
    <div class="brand-square"></div>
    <p class="brand-name brand-name__main">CORVELLE</p>
    <p class="brand-name brand-name__sub">VINEYARDS</p>
    <div class="varietal varietal--centered">
      <div class="varietal__name">MALBEC</div>
      <div class="varietal__origin">TEMECULA , CALIFORNIA</div>
    </div>
  </section>

  <section class="label label--cabernet">
    <div class="brand-square"></div>
    <p class="brand-name brand-name__main">CORVELLE</p>
    <p class="brand-name brand-name__sub">VINEYARDS</p>
    <div class="varietal varietal--centered">
      <div class="varietal__name">CABERNET SAUVIGNON</div>
      <div class="varietal__origin">TEMECULA , CALIFORNIA</div>
    </div>
  </section>

</main>
</body>
</html>
```